New Business Aquisition Postcard Project

Create a post card for new client acquisition. The postcard is to promote our new campaign, our BEAT YOUR RATE OR WE PAY THE TAB Campaign. We have preselected people that we know we are highly likely to save money. These people own homes, valued 100k or over, these homes were built after the year 2000 and are within a radius of our office. If we cannot save them $307 (the average savings experienced by our customers) a year on their home and auto insurance combined, we will send them a $20 gift card for wasting their time.

Target Market(s)

This mailing will be sent to confirmed homeowners in Western Pennsylvania. These people own a home built after the year 2000.

Industry/Entity Type

Car Insurance

Font styles to use
Serif

Colors
0355a3

Requirements
Must have
• I have included a picture of the flyer I created. We need to include testimonials. I have those on the flyer and more.
Nice to have
• This should be laid out and ready to go in a postcard format. I have not decided if I will use labels or just run the postcards through my printer to put the names on. Where the flyer uses a person's name, the postcard should use "Pennsylvania Homeowner". It could also say "Attention to Pennsylvania Homeowners with homes built after the year 2000." Remember, we have preselected this people and we can let them know that. This offer will only be going to highly qualified prospects and will not be plastered all over town, so to speak.

```html
<!DOCTYPE html>
<html lang="en">
<head>
<meta charset="utf-8">
<title>Miles Dunbar Agency – Homeowner Postcard</title>
<link href="https://fonts.googleapis.com/css2?family=Open+Sans:ital,wght@0,300;0,400;0,600;0,700;1,400;1,700&family=Alfa+Slab+One&family=Architects+Daughter&display=swap" rel="stylesheet">
<style>
  :root{
    --brand-blue:#0355a3;
    --navy:#0b1d6e;
    --sky:#1e88d8;
    --cyan:#2fc4f2;
    --lime:#c8f03a;
    --ink:#333a44;
    --muted:#7d8590;
    --agency:#8a96a6;
    --paper:#ffffff;
    --page:#ffffff;
    --rule:#b9c2cc;
  }
  *{box-sizing:border-box;margin:0;padding:0}
  html,body{width:933px;height:1200px;overflow:hidden;background:var(--page)}
  body{position:relative;font-family:"Open Sans",Arial,sans-serif;color:var(--ink)}

  .card{position:absolute;background:var(--paper);overflow:hidden;border:1px solid #e3e6ea}
  .card--front{left:33px;top:24px;width:868px;height:544px}
  .card--back{left:31px;top:586px;width:870px;height:580px}

  .card__art{position:absolute;inset:0}

  /* brand wordmark */
  .brand{position:absolute;color:var(--brand-blue);font-weight:300;white-space:nowrap;line-height:1}
  .brand__name{display:block}
  .brand__agency{position:absolute;right:0;bottom:100%;margin-bottom:2px;color:var(--agency);font-weight:300;line-height:1}

  /* front */
  .hero-photo{position:absolute;left:20px;top:10px;width:560px;height:460px;border-radius:6px;
    background:radial-gradient(ellipse at 40% 40%,#d9dde2 0%,#c4ccd6 45%,#eef1f4 100%)}
  .testimonial{position:absolute;left:318px;top:302px;display:flex;align-items:flex-start;gap:8px}
  .testimonial__mark{font-family:Georgia,serif;font-size:104px;line-height:.85;color:var(--sky);font-weight:700;width:78px}
  .testimonial__text{width:150px;border-left:2px solid var(--sky);padding-left:5px;
    font-size:11.3px;line-height:14px;font-style:italic;color:#3a4350}
  .card--front .brand{left:54px;top:478px;font-size:60px}
  .card--front .brand__agency{font-size:30px}

  .offer{position:absolute;left:548px;top:34px;width:312px;text-align:center;color:#fff}
  .offer__attention{font-family:"Alfa Slab One",Georgia,serif;font-size:35px;font-weight:400;color:var(--lime);letter-spacing:1px}
  .offer__audience{margin-top:12px;font-size:15.5px;font-weight:700;font-style:italic;line-height:24px}
  .offer__promise{margin-top:14px;font-family:"Architects Daughter",cursive;font-size:20px;line-height:33px}
  .cta{margin-top:14px;display:flex;flex-direction:column;align-items:center}
  .cta__row{display:flex;align-items:center;gap:8px}
  .cta__call{font-size:42px;font-weight:700;font-style:italic;color:var(--cyan);line-height:1;letter-spacing:-1px}
  .cta__quote{font-family:"Alfa Slab One",Georgia,serif;font-size:20px;color:var(--lime);margin-top:4px}
  .offer__phone{margin-top:20px;font-size:31px;font-weight:600;letter-spacing:.5px}
  .offer__web{margin-top:4px;font-size:16.5px;font-weight:700;letter-spacing:.5px}

  /* back */
  .card--back .brand{left:54px;top:84px;font-size:44px}
  .card--back .brand__agency{font-size:22px}
  .letter{position:absolute;left:28px;top:152px;width:392px;font-size:12.6px;line-height:18px;color:#3a3f46}
  .letter p{margin-bottom:8px}
  .letter__cta{font-weight:700}
  .letter__sign{margin:-2px 0 0 210px;font-family:"Architects Daughter",cursive;color:var(--brand-blue);font-size:16px}
  .quotes-art{position:absolute;left:30px;top:440px;width:150px;height:100px;border-radius:8px;
    background:linear-gradient(135deg,#2e7de0,#a9c9ee 70%,#e9eef4)}
  .quotes-box{position:absolute;left:176px;top:450px;width:222px;height:96px;border:2px solid var(--sky);
    border-left:none;border-radius:0 10px 10px 0;padding:2px 0 0 52px}
  .quotes-box__title{font-size:20px;font-weight:700;color:var(--sky);line-height:24px}
  .quotes-box__title span{color:var(--muted);font-weight:600}
  .quotes-box ul{list-style:none;font-size:16px;font-weight:700;line-height:19px}
  .quotes-box li::before{content:"✓";margin-right:12px;font-weight:400}
  .quotes-box li{color:var(--sky)}
  .quotes-box li.is-muted{color:var(--muted)}

  .return-address{position:absolute;left:474px;top:68px;font-size:12.6px;line-height:18px;color:#3a3f46;font-style:normal}
  .stamp-box{position:absolute;left:762px;top:64px;width:104px;height:88px;border:1px dashed #aab2bb}
  .mail-line{position:absolute;left:504px;width:340px;border-top:1px dashed var(--rule)}
  .mail-line--1{top:318px}
  .mail-line--2{top:380px}
  .mail-line--3{top:442px}
</style>
</head>
<body>

<section class="card card--front" aria-label="Postcard front">
  <div class="hero-photo" role="img" aria-label="Photo of a two-storey suburban home, a dark blue SUV and a smiling family sitting together"></div>
  <svg class="card__art" viewBox="0 0 868 544" width="868" height="544" aria-hidden="true">
    <defs>
      <linearGradient id="panel" x1="0" y1="0" x2="1" y2="1">
        <stop offset="0" stop-color="#0b1d6e"/>
        <stop offset=".6" stop-color="#0a3f9c"/>
        <stop offset="1" stop-color="#0355a3"/>
      </linearGradient>
    </defs>
    <path d="M474 0 C548 120 588 380 543 544 L868 544 L868 0 Z" fill="#1e88d8"/>
    <path d="M487 0 C560 120 600 380 555 544 L868 544 L868 0 Z" fill="url(#panel)"/>
  </svg>
  <div class="testimonial">
    <div class="testimonial__mark">“</div>
    <p class="testimonial__text">“Miles helped us SAVE $642 per year on our auto and home insurance. He simplified our three policies, got us a new low monthly payment, all while increasing our coverages.”</p>
  </div>
  <div class="brand"><span class="brand__agency">AGENCY</span><span class="brand__name">MILES DUNBAR</span></div>

  <div class="offer">
    <h1 class="offer__attention">ATTENTION!</h1>
    <p class="offer__audience">PENNSYLVANIA HOMEOWNERS WITH<br>HOMES BUILT AFTER THE YEAR 2000:</p>
    <p class="offer__promise">“If I Can’t Save You At<br>Least $307.00 Per Year on<br>Your Auto and Home<br>Insurance, I’ll Pay You $20!”</p>
    <div class="cta">
      <div class="cta__row">
        <svg width="32" height="38" viewBox="0 0 24 28" aria-hidden="true"><path d="M6 2c-2 1-4 3-4 6 0 8 6 16 14 18 3 1 5-1 6-3l-4-4-3 2c-3-2-6-6-7-9l2-3-4-5z" fill="#2fc4f2"/></svg>
        <span class="cta__call">Call NOW</span>
      </div>
      <span class="cta__quote">GET A QUOTE!</span>
    </div>
    <p class="offer__phone">(555) 014-2290</p>
    <p class="offer__web">WWW.QUOTEMEMILES.COM</p>
  </div>
</section>

<section class="card card--back" aria-label="Postcard back">
  <svg class="card__art" viewBox="0 0 870 580" width="870" height="580" aria-hidden="true">
    <path d="M392 0 C440 130 445 400 432 580 L440 580 C455 400 452 130 412 0 Z" fill="#1e88d8"/>
    <path d="M412 0 C452 130 455 400 440 580 L444 580 C462 400 460 130 424 0 Z" fill="#0355a3"/>
  </svg>
  <div class="brand"><span class="brand__agency">AGENCY</span><span class="brand__name">MILES DUNBAR</span></div>
  <div class="letter">
    <p>Dear Homeowner,</p>
    <p>The auto &amp; home insurance carriers I work with just LOWERED RATES in Pennsylvania! We’ve been helping your neighbors save hundreds of dollars per year.</p>
    <p>In fact, I’m so confident I can save you money… If I can’t save you at least $307.00 - I’ll pay you $20 as my penalty just for wasting your time. (You just need to qualify for auto and home insurance.)</p>
    <p>ONE CALL DOES IT ALL! We’ll cancel your existing policies for you, request any refund you may be owed, PLUS notify DMV, your bank, and contact your mortgage company for escrow payment, so the process is easy and pain-free for you!!</p>
    <p class="letter__cta">Call (555) 014-2290 or visit QUOTEMEMILES.COM!</p>
    <p class="letter__sign">Miles Dunbar</p>
  </div>
  <div class="quotes-art" role="img" aria-label="Illustration of a small blue house and a blue car"></div>
  <div class="quotes-box">
    <h2 class="quotes-box__title">OUR <span>QUOTES</span></h2>
    <ul>
      <li>Fast</li>
      <li class="is-muted">Free</li>
      <li>Easy</li>
    </ul>
  </div>
  <address class="return-address">418 Linden Court<br>Maple Ridge, PA 15999<br>(555) 014-2290<br>QUOTEMEMILES.COM</address>
  <div class="stamp-box" aria-label="Stamp area"></div>
  <div class="mail-line mail-line--1"></div>
  <div class="mail-line mail-line--2"></div>
  <div class="mail-line mail-line--3"></div>
</section>

</body>
</html>
```